Gantry Moss Website Using Wordpress Jetpack CMS

Design a responsive SEO enabled website using Wordpress theme. 7 Pages with content to be developed. Primarily a single page site using Wordpress, so seeking a string website developer with capable skills in native understanding of SEO.

Unique Value Proposition
Sports Clubs are built on passion, people and facilities. All the volunteering and dedication in the world is limited by the level of quality services and benefits that are available to member. Access to funds and lack of knowledge create a void that holds back Club growth and access to improved facilities. Improved facilities draw members and discretionary spend to clubs, but Clubs are challenged in easily delivering expensive facility upgrades. We solve that problem in a way that's easy to digest and meets all the things considered and many that have not been considered at all!

High Level Concept
Gantry Moss seeks to solve a growing problem. How do clubs remain viable? How do clubs increase participation? How do clubs provide exceptional value for their members discretionary expenditure?

The heart of any solid sporting club is its people, volunteers all over the world, trying to make a difference.

Gantry Moss was built to facilitate Club growth by providing state of the art facilities without any capital exposure, in fact by providing a shared revenue model that allows for additional facilities to be layered on top of existing ones. Linking in an energy transfer scheme from the excess energy released in peak, the model allows extension to Club Member Energy Offers which exponentially grows revenues and provides strong fiscal opportunity back to the club.

At the centre of Gantry moss are Lights and Power which are a primary life blood of every club, particularly sports clubs offering training and coaching, like tennis, soccer, rugby lawn bowls, cricket and aussie rules to name a few

With energy bills reaching in excess of $10,000 per annum in many clubs, Gantry Moss aims to facilitate an energy performance contract for sports clubs that provides new facilities without financial exposure and a profit share on asset placement. This makes decision making easier for volunteer committees

Problems in Clubs
Membership and Participation
Attracting members and ensuring they get appropriate bang for buck takes time, energy and resources. Members seek quality environments with structured sport and easy access to sport facilities at times that suit.

Funding of Capital Assets
Clubs have considerable expenditure in infrastructure to ensure high quality facilities are upgraded and maintained.

Managing The Club
Clubs have considerable expenditure in day to day costs and unpaid volunteers are needed to maintain membership numbers and ensure high quality facilities and available.

The Solution
COST NEUTRAL INFRASTRUCTURE
Assess Power Expenditure
Identify Facilities Improvements - Value Adds etc
Provide Best Outcome Funding Model (Off Grid), Future Asset Returns, Booking/Club Mgnt
Deploy and Maintain Assets, Lower Maintenance

NEXT GEN ENERGY RETAIL SPONSORSHIP
Recover ZORN credits
Negotiate on Grid Sales
Develop Finance and Energy Rebates
Leverage Trading Mechanism

CLUB & MEMBER BENEFITS
Sponsor through Energy Purchase
Members Benefits in Offset Costs and Club Kickback
Giving Back drives the Club Improvement Plan and Income Generation + Carbon Neutral

Target Market(s)

Sports Clubs, Sports Club Committees, Local Councils looking to upgrade local club facilities

Coding

Coded - Design and coding required

Number of Pages Required

5+ page

Font styles to use
Sans Serif

Colors
acd036
848484

Requirements
Must have
• Responsive Design
• Must use Wordpress Jetpack for Delivery
• Target to use Theme with single page
• CMS for custom content additions
• Existing Domain
• Landing Pages
Nice to have
• https://www.quenmarix.com/en_AU/stillcore is an example of a site that displays characteristics
• Clean colour per logo and ability to expand easily using Wordpress
Should not have
• Hardcoded elements. CMS is a MUST HAVE

```html
<!DOCTYPE html>
<html lang="en">
<head>
<meta charset="utf-8">
<title>Gantry Moss</title>
<link href="https://fonts.googleapis.com/css2?family=Montserrat:wght@400;600;700;800&family=Open+Sans:wght@400;600&display=swap" rel="stylesheet">
<style>
:root{
  --green:#acd036;
  --green-dark:#8db324;
  --grey:#848484;
  --ink:#222;
  --night:#0b1424;
  --footer:#161819;
  --white:#fff;
  --blue:#1e73d8;
}
*{box-sizing:border-box;margin:0;padding:0}
html,body{width:1200px;height:3300px;overflow:hidden}
body{font-family:"Open Sans",Arial,sans-serif;color:var(--ink);background:var(--white);position:relative}
h1,h2,h3,h4,.btn,.nav a,.brand{font-family:"Montserrat",Arial,sans-serif}
.btn{display:inline-block;background:var(--green);color:var(--white);font-size:15px;font-weight:600;padding:12px 28px;border-radius:30px;text-transform:uppercase;letter-spacing:.5px}
.btn-outline{background:transparent;color:var(--green-dark);border:2px solid var(--green);padding:8px 22px;font-size:13px}
.brand{display:flex;align-items:center;gap:12px;color:var(--green);font-weight:800;font-size:34px;letter-spacing:-.5px}
.brand-mark{width:30px;height:30px;border-radius:50%;background:var(--green)}

/* hero */
.hero{position:absolute;top:0;left:0;width:1200px;height:760px;overflow:hidden}
.hero-scene{position:absolute;inset:0;background:linear-gradient(180deg,#0a1a3a 0%,#1b3a6e 35%,#26507f 55%,#3c6a3a 75%,#2f6e2a 100%)}
.hero .brand{position:absolute;top:34px;left:110px}
.nav{position:absolute;top:70px;right:120px;display:flex;align-items:center;gap:38px}
.nav a{color:var(--white);font-size:16px;font-weight:600;text-decoration:none}
.nav .signin{border:2px solid var(--white);background:var(--blue);padding:8px 20px;border-radius:24px;font-size:13px}
.hero-text{position:absolute;top:320px;width:100%;text-align:center;color:var(--white)}
.hero-text h1{font-size:72px;font-weight:800;letter-spacing:1px}
.hero-text p{font-size:18px;margin:16px 0 30px}
.chevron{position:absolute;top:684px;left:584px;width:32px;height:32px;border-radius:50%;background:var(--white);display:flex;align-items:center;justify-content:center}
.side-stripe{position:absolute;background:var(--green)}

/* welcome */
.welcome{position:absolute;top:760px;left:0;width:1200px;height:912px;text-align:center}
.section-dot{width:60px;height:60px;border-radius:50%;border:8px solid #444;margin:60px auto 0}
.welcome h2,.provide h2{font-size:46px;font-weight:600;color:#333;margin-top:40px;letter-spacing:.5px}
.accent{color:var(--green)}
.welcome .lead{width:960px;margin:20px auto 0;color:var(--grey);font-size:14px;line-height:24px}
.cards{position:absolute;top:360px;left:112px;display:flex;gap:96px}
.card{width:280px;text-align:left}
.card-photo{height:210px;background:linear-gradient(180deg,#071a3c 0%,#1d4f95 45%,#2d7d3a 80%,#3c8b2c 100%)}
.card h3{font-size:17px;font-weight:700;color:#333;margin:14px 0 8px}
.card p{font-size:13px;color:var(--grey);line-height:21px}
.card .btn-outline{margin-top:14px}
.card-feature{height:440px;position:relative;background:linear-gradient(180deg,#0a1a3a 0%,#163c6d 40%,#1f6d2c 70%,#2d7d2a 100%);padding:210px 20px 0}
.card-feature p{color:var(--white);font-size:14px;font-weight:600;line-height:22px}
.card-feature .btn{margin-top:20px;padding:8px 20px;font-size:12px;background:transparent;border:2px solid var(--white)}

/* serve */
.serve{position:absolute;top:1672px;left:0;width:1200px;height:448px;background:radial-gradient(ellipse at 50% 70%,#1f4d2a 0%,#0c1f2a 40%,#050b12 100%);text-align:center;color:var(--white);overflow:hidden}
.serve-scene{position:absolute;inset:0;background:radial-gradient(ellipse at 30% 25%,rgba(110,170,255,.35),transparent 25%),radial-gradient(ellipse at 70% 25%,rgba(110,170,255,.35),transparent 25%)}
.serve h2{position:relative;font-size:46px;font-weight:700;margin-top:160px}
.serve p{position:relative;font-size:20px;margin:16px 0 26px}
.serve .btn{position:relative}

/* provide */
.provide{position:absolute;top:2120px;left:0;width:1200px;height:820px;text-align:center}
.provide h2{font-weight:700}
.solar{position:absolute;top:440px;left:120px;width:440px;height:280px;background:linear-gradient(160deg,#2a3f7a 0%,#1c2b58 50%,#aab3c2 100%);clip-path:polygon(20% 0,100% 15%,80% 100%,0 75%)}
.features{position:absolute;top:380px;left:610px;text-align:left;width:480px}
.feature{display:flex;gap:28px;margin-bottom:40px}
.feature-icon{flex:none;width:80px;height:80px;border-radius:50%;border:3px solid #ddd;display:flex;align-items:center;justify-content:center}
.feature h4{font-size:16px;font-weight:700;color:#333;margin:10px 0 6px}
.feature p{font-size:13px;color:var(--grey);line-height:21px}

/* newsletter + footer */
.newsletter{position:absolute;top:2940px;left:0;width:1200px;height:60px;background:#1e2426;display:flex;align-items:center;padding:0 130px}
.newsletter h3{color:var(--green);font-size:24px;font-weight:600;letter-spacing:1px;width:350px}
.signup{display:flex;border-radius:24px;overflow:hidden;height:38px}
.signup span{background:var(--white);color:var(--grey);width:460px;padding:0 20px;line-height:38px;font-size:14px}
.signup b{background:#2a2f31;color:var(--white);padding:0 22px;line-height:38px;font-size:13px;font-family:"Montserrat",sans-serif}
.footer{position:absolute;top:3000px;left:0;width:1200px;height:300px;background:var(--footer);color:var(--white);overflow:hidden}
.footer .brand{position:absolute;top:90px;left:130px}
.follow{position:absolute;top:70px;left:440px}
.follow h4{font-size:20px;font-weight:700;margin-bottom:16px}
.socials{display:flex;gap:12px}
.socials i{width:32px;height:32px;border-radius:50%;background:var(--white);display:block}
.footer .contact{position:absolute;top:100px;right:140px}
.copyright{position:absolute;top:255px;width:100%;text-align:center;font-size:13px;color:#ccc}
</style>
</head>
<body>

<header class="hero">
  <div class="hero-scene" role="img" aria-label="Floodlit stadium at night with a green pitch"></div>
  <div class="side-stripe" style="left:0;top:180px;width:60px;height:580px;clip-path:polygon(0 0,100% 20%,30% 100%,0 100%)"></div>
  <div class="side-stripe" style="right:0;top:180px;width:60px;height:580px;clip-path:polygon(100% 0,100% 100%,70% 100%,0 20%)"></div>
  <div class="brand"><span class="brand-mark"></span>Gantry Moss</div>
  <nav class="nav">
    <a href="#">Home</a><a href="#">About us</a><a href="#">Services</a><a href="#">Events</a><a href="#">Blog</a><a href="#">Contact</a><a href="#" class="signin">SIGN IN</a>
  </nav>
  <div class="hero-text">
    <h1>GANTRY MOSS</h1>
    <p>Temporibus autem quibusdam et aut officiis debitis aut rerum necessitatibus saepe eveniet</p>
    <span class="btn">Book online</span>
  </div>
  <div class="chevron"><svg width="14" height="10" viewBox="0 0 14 10"><path d="M2 2l5 5 5-5" stroke="#333" stroke-width="2" fill="none"/></svg></div>
</header>

<section class="welcome">
  <div class="section-dot"></div>
  <h2>WELCOME TO <span class="accent">GANTRY MOSS</span></h2>
  <p class="lead">Sed ut perspiciatis unde omnis iste natus error sit voluptatem accusantium doloremque laudantium, totam rem aperiam, eaque ipsa quae ab illo inventore veritatis et quasi architecto beatae vitae dicta sunt explicabo. Nemo enim ipsam voluptatem quia voluptas sit aspernatur aut odit aut fugit, sed quia consequuntur magni dolores eos.</p>
  <div class="cards">
    <article class="card card-feature" role="img" aria-label="Night sports field under floodlights">
      <p>We provide a lighting and power system for sports clubs supported by access control and secure online bookings for club hire and court/light usage.</p>
      <span class="btn">Read more</span>
    </article>
    <article class="card">
      <div class="card-photo" role="img" aria-label="Stadium floodlights over a green pitch"></div>
      <h3>Sed quia consequuntur</h3>
      <p>Ut enim ad minima veniam, quis nostrum exercitationem ullam corporis suscipit laboriosam, nisi ut aliquid ex ea commodi.</p>
      <span class="btn btn-outline">Read more</span>
    </article>
    <article class="card">
      <div class="card-photo" role="img" aria-label="Bright stadium lights above the field"></div>
      <h3>Exercitationem ullorporis</h3>
      <p>Ut enim ad minima veniam, quis nostrum exercitationem ullam corporis suscipit laboriosam, nisi ut aliquid ex ea commodi.</p>
      <span class="btn btn-outline">Read more</span>
    </article>
  </div>
</section>

<section class="serve">
  <div class="serve-scene" role="img" aria-label="Floodlights shining over a dark stadium"></div>
  <div class="side-stripe" style="left:0;top:60px;width:90px;height:330px;clip-path:polygon(0 0,100% 30%,20% 100%,0 100%)"></div>
  <div class="side-stripe" style="right:0;top:60px;width:90px;height:330px;clip-path:polygon(100% 0,100% 100%,80% 100%,0 30%)"></div>
  <h2>WHERE WE SERVE</h2>
  <p>Our target customers are Sports Clubs, Sports Club Committees, Councils</p>
  <span class="btn">Book online</span>
</section>

<section class="provide">
  <div class="section-dot"></div>
  <h2>WHAT <span class="accent">WE PROVIDE</span></h2>
  <div class="solar" role="img" aria-label="Solar panel"></div>
  <div class="features">
    <div class="feature">
      <div class="feature-icon"><svg width="30" height="30" viewBox="0 0 30 30"><circle cx="15" cy="12" r="8" fill="none" stroke="#f2a33a" stroke-width="2.5"/><rect x="11" y="21" width="8" height="5" fill="#8a5a2b"/></svg></div>
      <div><h4>ART LIGHTS</h4><p>Sed ut perspiciatis unde omnis iste natus error sit voluptatem accusantium doloremque laudantium totam.</p></div>
    </div>
    <div class="feature">
      <div class="feature-icon"><svg width="34" height="26" viewBox="0 0 34 26"><path d="M6 2h26l-4 22H2z" fill="#2a4a8a"/><path d="M12 2l-3 22M20 2l-3 22M4 13h28" stroke="#fff" stroke-width="1.5"/></svg></div>
      <div><h4>SOLAR TECHNOLOGY</h4><p>Sed ut perspiciatis unde omnis iste natus error sit voluptatem accusantium doloremque laudantium totam.</p></div>
    </div>
    <div class="feature">
      <div class="feature-icon"><svg width="22" height="34" viewBox="0 0 22 34"><rect x="7" y="0" width="8" height="4" fill="#8a5a2b"/><rect x="1" y="4" width="20" height="29" rx="2" fill="none" stroke="#8a5a2b" stroke-width="2.5"/><rect x="5" y="16" width="12" height="13" fill="#f2a33a"/></svg></div>
      <div><h4>BATTERY TECHNOLOGY</h4><p>Sed ut perspiciatis unde omnis iste natus error sit voluptatem accusantium doloremque laudantium totam.</p></div>
    </div>
  </div>
</section>

<section class="newsletter">
  <h3>SIGN UP NEWSLETTER</h3>
  <div class="signup"><span>Enter Email</span><b>SUBSCRIBE</b></div>
</section>

<footer class="footer">
  <div class="side-stripe" style="left:0;top:0;width:80px;height:300px;clip-path:polygon(0 0,100% 0,30% 100%,0 100%)"></div>
  <div class="side-stripe" style="right:0;top:0;width:80px;height:300px;clip-path:polygon(0 0,100% 0,100% 100%,70% 100%)"></div>
  <div class="brand"><span class="brand-mark"></span>Gantry Moss</div>
  <div class="follow">
    <h4>Follow us :</h4>
    <div class="socials"><i></i><i></i><i></i><i></i><i></i><i></i><i></i></div>
  </div>
  <span class="btn contact">Contact us now</span>
  <p class="copyright">© copyright 2018 Gantry Moss All Rights Reserved &nbsp;|&nbsp; Privacy policy &nbsp;|&nbsp; Terms and use</p>
</footer>

</body>
</html>
```